TBrenwick Business Cards & Letterhead

I have a logo but need a design for some new business cards. We are a Design-Build Firm that specializes in the design and construction of commercial projects.
the cards need to be professional. no cartoon stuff.
i would like to have the cards in AI format so I can update the card as needed. Logo is provided.
Our Address is: 4718 Fenmoor Ct. Cary, North Carolina 27513

```html
<!DOCTYPE html>
<html lang="en">
<head>
<meta charset="utf-8">
<title>TBrenwick Business Card</title>
<link rel="stylesheet" href="https://fonts.googleapis.com/css2?family=Lato:wght@400;700;900&display=swap">
<style>
  :root {
    --page: #1b1b1b;
    --card: #2a2a2a;
    --accent: #1a78c2;
    --text: #f2f2f2;
    --muted: #bdbdbd;
  }
  * { margin: 0; padding: 0; box-sizing: border-box; }
  html, body { width: 1200px; height: 875px; overflow: hidden; }
  body {
    background: var(--page);
    font-family: "Lato", sans-serif;
    position: relative;
  }
  .card {
    position: absolute;
    width: 520px;
    height: 297px;
    background: var(--card);
    border-radius: 18px;
  }
  .card-front { left: 60px; top: 130px; }
  .card-back { left: 620px; top: 450px; }

  .brand {
    position: absolute;
    inset: 0;
    display: flex;
    align-items: center;
    justify-content: center;
    gap: 14px;
  }
  .brand-square {
    width: 34px; height: 34px;
    background: var(--accent);
  }
  .brand-name {
    font-weight: 900;
    font-size: 50px;
    letter-spacing: 2px;
    color: var(--muted);
    text-transform: uppercase;
  }

  .identity {
    position: absolute;
    right: 250px;
    top: 118px;
    text-align: right;
  }
  .identity-name {
    font-weight: 900;
    font-size: 27px;
    color: var(--accent);
    text-transform: uppercase;
    letter-spacing: 0.5px;
    line-height: 1;
  }
  .identity-role {
    font-size: 15px;
    color: var(--text);
    margin-top: 5px;
  }
  .divider {
    position: absolute;
    left: 282px;
    top: 70px;
    width: 1px;
    height: 150px;
    background: var(--accent);
  }
  .contact {
    position: absolute;
    left: 300px;
    top: 74px;
    list-style: none;
    font-size: 12.5px;
    color: var(--text);
    line-height: 1.35;
  }
  .contact li {
    display: flex;
    align-items: flex-start;
    gap: 8px;
    white-space: nowrap;
  }
  .contact li + li { margin-top: 3px; }
  .contact .address { margin-bottom: 6px; }
  .contact svg {
    width: 11px; height: 11px;
    flex: none;
    margin-top: 3px;
    fill: var(--accent);
  }
</style>
</head>
<body>
  <section class="card card-front">
    <div class="brand">
      <span class="brand-square"></span>
      <span class="brand-name">TBrenwick</span>
    </div>
  </section>

  <section class="card card-back">
    <div class="identity">
      <div class="identity-name">Daniel Harlow</div>
      <div class="identity-role">Founder &amp; CEO</div>
    </div>
    <div class="divider"></div>
    <ul class="contact">
      <li class="address">
        <svg viewBox="0 0 12 12"><path d="M6 0a4 4 0 0 0-4 4c0 3 4 8 4 8s4-5 4-8a4 4 0 0 0-4-4zm0 5.5A1.5 1.5 0 1 1 6 2.5a1.5 1.5 0 0 1 0 3z"/></svg>
        <span>4718 Fenmoor Ct. Cary<br>North Carolina 27513</span>
      </li>
      <li>
        <svg viewBox="0 0 12 12"><path d="M2.5 0.5l2 2-1 1.5c.8 1.7 2 2.9 3.5 3.5l1.5-1 2 2-1.5 2C4.5 10 1.5 7 0.5 2z"/></svg>
        <span>(919) 555-0142</span>
      </li>
      <li>
        <svg viewBox="0 0 12 12"><path d="M3 0h6v12H3zM4 1.5v8h4v-8z"/></svg>
        <span>(919) 555-0187</span>
      </li>
      <li>
        <svg viewBox="0 0 12 12"><path d="M3 0h6v3H3zM1 4h10v5H9v3H3V9H1zm3 3v4h4V7z"/></svg>
        <span>(919) 555-0163</span>
      </li>
      <li>
        <svg viewBox="0 0 12 12"><path d="M0 2h12v8H0zm1 1l5 3.5L11 3z"/></svg>
        <span>office@tbrenwickbuild.com</span>
      </li>
      <li>
        <svg viewBox="0 0 12 12"><circle cx="6" cy="6" r="6"/></svg>
        <span>www.tbrenwickbuild.com</span>
      </li>
    </ul>
  </section>
</body>
</html>
```